Business Card and Staionary Package for A Landscape Design Build Company
Silver Fern Yardworks Co, LLC.
Bright & Fun-filled
Neil P. Beckett, BLA, NHPA
Owner
(2) Locations P.O Box 4187 Gulfport, Mississippi 39506 P.O. Box 5903 Mobile, Alabama 36619
MS Office (228)-631-2947; AL Office (251)-749-3368
mbeckett@silverfernyardworks.example
silverfernyardworks.example
MS Contractor # 52819-SC; MS Landscape #LT214; AL Landscape # PSH-3561; NHPA Certififed Installer
Open to all design suggestion, please feel free to use your own ideas.

```html
<!DOCTYPE html>
<html lang="en">
<head>
<meta charset="utf-8">
<title>Silver Fern Yardworks Co — Business Card</title>
<link rel="stylesheet" href="https://fonts.googleapis.com/css2?family=Cinzel:wght@400;700&family=Cormorant+Garamond:wght@500;600&display=swap">
<style>
  :root {
    --leaf: #7cc243;
    --leaf-light: #a6d97a;
    --bark: #5b3f22;
    --ink: #4a4a4a;
    --paper: #ffffff;
    --backdrop: #e9ebe8;
  }
  * { margin: 0; padding: 0; box-sizing: border-box; }
  html, body { width: 1200px; height: 1009px; overflow: hidden; }
  body {
    background: var(--backdrop);
    position: relative;
    font-family: "Cormorant Garamond", Georgia, serif;
    color: var(--ink);
  }
  .card {
    position: absolute;
    left: 220px;
    width: 760px;
    height: 434px;
    border-radius: 26px;
    overflow: hidden;
    box-shadow: 0 6px 18px rgba(0,0,0,0.15);
  }
  .card--back { top: 40px; background: var(--leaf); }
  .card--front { top: 535px; background: var(--paper); }

  .back-web {
    position: absolute;
    left: 26px; top: 40px;
    transform-origin: left top;
    transform: rotate(90deg) translate(0, -14px);
    font-family: "Cinzel", Georgia, serif;
    font-size: 13px;
    letter-spacing: 2px;
    color: rgba(255,255,255,0.8);
    white-space: nowrap;
  }
  .back-mark {
    position: absolute;
    right: 90px; top: 120px;
    width: 210px; height: 210px;
    border-radius: 50%;
    background: var(--leaf-light);
    opacity: 0.6;
  }

  .front-wave { position: absolute; left: 0; bottom: 0; width: 760px; height: 434px; }

  .brand {
    position: absolute;
    left: 38px; top: 92px;
    width: 270px;
    display: flex; align-items: center; gap: 14px;
  }
  .brand-dot {
    flex: none;
    width: 46px; height: 46px;
    border-radius: 50%;
    background: var(--leaf);
  }
  .brand-name {
    font-family: "Cinzel", Georgia, serif;
    font-weight: 700;
    font-size: 25px;
    line-height: 1.1;
    color: var(--bark);
  }

  .divider {
    position: absolute;
    left: 330px; top: 70px;
    width: 1.5px; height: 210px;
    background: var(--bark);
  }

  .contact {
    position: absolute;
    left: 352px; top: 66px;
    font-size: 13px;
    line-height: 1.32;
  }
  .contact-name {
    font-family: "Cinzel", Georgia, serif;
    font-size: 20px;
    color: var(--leaf);
    margin-bottom: 2px;
  }
  .contact-role { font-weight: 600; margin-bottom: 6px; }
  .contact-label { color: var(--leaf); font-weight: 600; }
  .contact-block { margin-bottom: 5px; }
</style>
</head>
<body>

<section class="card card--back" aria-label="Card back">
  <p class="back-web">silverfernyardworks.example</p>
  <div class="back-mark"></div>
</section>

<section class="card card--front" aria-label="Card front">
  <svg class="front-wave" viewBox="0 0 760 434" aria-hidden="true">
    <path d="M0 300 C180 250 330 330 500 330 C620 330 700 300 760 290 L760 434 L0 434 Z" fill="var(--leaf)"/>
    <path d="M0 292 C170 232 340 320 500 318 C620 316 700 282 760 272" fill="none" stroke="var(--bark)" stroke-width="6"/>
    <path d="M0 312 C200 270 330 345 520 340 C640 336 710 310 760 302" fill="none" stroke="var(--bark)" stroke-width="3"/>
  </svg>

  <div class="brand">
    <span class="brand-dot"></span>
    <span class="brand-name">Silver Fern Yardworks Co</span>
  </div>

  <div class="divider"></div>

  <div class="contact">
    <p class="contact-name">Neil P. Beckett, BLA, NHPA</p>
    <p class="contact-role">Owner</p>
    <div class="contact-block">
      <p>P.O Box 4187, Gulfport, Mississippi 39506</p>
      <p>P.O. Box 5903, Mobile, Alabama 36619</p>
    </div>
    <div class="contact-block">
      <p><span class="contact-label">MS Office</span> (228)-631-2947</p>
      <p><span class="contact-label">AL Office</span> (251)-749-3368</p>
    </div>
    <div class="contact-block">
      <p>mbeckett@silverfernyardworks.example</p>
      <p>silverfernyardworks.example</p>
    </div>
    <p>MS Contractor # 52819-SC &middot; MS Landscape # LT214</p>
    <p>AL Landscape # PSH-3561 &middot; NHPA Certified Installer</p>
  </div>
</section>

</body>
</html>
```